I am a highly experienced private practice psychotherapist serving high end clientele in the Wall Street area of New York City. I need electronic letterhead (that can also be printed) to use for bills, receipts, and correspondences.

My clients are very high end and are used to elegance and wealth. The letterhead should contain the following information: Marissa K. Tolland, LCSW 57 Pinegate Avenue, Suite 2716 New York, NY 10392 Phone : (917) 555-3179 email: therapy@marissatollandlcsw.example website: www.marissatollandlcsw.example

Thank you for your designs. Please be advised that the letterhead will be used for bills/invoices; professional letters to other mental health professionals and doctors, as well as to attorneys. It needs to be highly professional in the same way that a law firm has professional and elegant letterhead, raher than whimsical or with spa designers. My letters end up as official documents.

```html
<!DOCTYPE html>
<html lang="en">
<head>
<meta charset="utf-8">
<title>Marissa K. Tolland, LCSW — Letterhead</title>
<link rel="stylesheet" href="https://fonts.googleapis.com/css2?family=Source+Sans+3:wght@400;600;700&display=swap">
<style>
  :root {
    --plum: #93177e;
    --ink: #111111;
    --paper: #ffffff;
    --backdrop: #e9e7e4;
    --rule-shadow: rgba(0, 0, 0, 0.22);
  }
  * { box-sizing: border-box; margin: 0; padding: 0; }
  html, body {
    width: 1132px;
    height: 1200px;
    overflow: hidden;
    background: var(--backdrop);
    font-family: "Source Sans 3", "Myriad Pro", Arial, sans-serif;
  }
  .letterhead {
    position: absolute;
    left: 102px;
    top: 0;
    width: 928px;
    height: 1200px;
    background: var(--paper);
    box-shadow: 0 0 18px rgba(0, 0, 0, 0.12);
  }
  .masthead {
    position: absolute;
    left: 42px;
    top: 36px;
    color: var(--plum);
  }
  .masthead__name {
    font-size: 31px;
    font-weight: 700;
    line-height: 1.05;
    letter-spacing: 0.1px;
  }
  .masthead__credential {
    font-size: 19px;
    font-weight: 400;
    line-height: 1.15;
  }
  .masthead__rule {
    position: absolute;
    left: 0;
    top: 108px;
    width: 340px;
    height: 14px;
  }
  .contact-bar {
    position: absolute;
    left: 28px;
    right: 28px;
    bottom: 50px;
    display: flex;
    justify-content: space-between;
    align-items: center;
    color: var(--plum);
    font-size: 12.5px;
    font-weight: 600;
    white-space: nowrap;
  }
  .contact-bar__item {
    display: flex;
    align-items: center;
    gap: 4px;
  }
  .contact-bar__icon {
    width: 15px;
    height: 15px;
    flex: none;
    fill: var(--plum);
  }
  .footer-band {
    position: absolute;
    left: 0;
    right: 0;
    bottom: 0;
  }
  .footer-band__rule {
    height: 7px;
    background: var(--ink);
  }
  .footer-band__gap {
    height: 3px;
    background: var(--paper);
  }
  .footer-band__fill {
    height: 26px;
    background: var(--plum);
  }
</style>
</head>
<body>
  <main class="letterhead">
    <header class="masthead">
      <h1 class="masthead__name">Marissa K. Tolland</h1>
      <p class="masthead__credential">LCSW</p>
    </header>
    <svg class="masthead__rule" viewBox="0 0 340 14" preserveAspectRatio="none" aria-hidden="true">
      <defs>
        <linearGradient id="ruleFade" x1="0" y1="0" x2="1" y2="0">
          <stop offset="0" stop-color="#000" stop-opacity="0"/>
          <stop offset="0.35" stop-color="#000" stop-opacity="0.22"/>
          <stop offset="0.75" stop-color="#000" stop-opacity="0.12"/>
          <stop offset="1" stop-color="#000" stop-opacity="0"/>
        </linearGradient>
      </defs>
      <path d="M0 2 Q170 -1 340 6 Q170 10 0 12 Z" fill="url(#ruleFade)"/>
    </svg>

    <footer>
      <address class="contact-bar" style="font-style:normal">
        <span class="contact-bar__item">
          <svg class="contact-bar__icon" viewBox="0 0 16 16" aria-hidden="true">
            <rect x="1" y="1" width="14" height="14" rx="3"/>
            <path d="M5.2 3.6c.4-.2.8 0 1 .4l.7 1.6c.1.3 0 .7-.3.9l-.7.5c.5 1.2 1.4 2.2 2.6 2.8l.5-.7c.2-.3.6-.4.9-.3l1.6.7c.4.2.6.6.4 1l-.4 1c-.2.5-.8.8-1.3.7C6.9 11.6 4.5 9.2 3.8 5.9c-.1-.5.2-1.1.7-1.3z" fill="#fff"/>
          </svg>
          (917) 555-3179
        </span>
        <span class="contact-bar__item">
          <svg class="contact-bar__icon" viewBox="0 0 16 16" aria-hidden="true">
            <path d="M8 0.5a5.5 5.5 0 0 0-5.5 5.5c0 4 5.5 9.5 5.5 9.5s5.5-5.5 5.5-9.5A5.5 5.5 0 0 0 8 0.5zm0 7.7a2.2 2.2 0 1 1 0-4.4 2.2 2.2 0 0 1 0 4.4z"/>
          </svg>
          57 Pinegate Avenue, Suite 2716 New York, NY 10392
        </span>
        <span class="contact-bar__item">
          <svg class="contact-bar__icon" viewBox="0 0 16 16" aria-hidden="true">
            <circle cx="8" cy="8" r="7"/>
            <g fill="none" stroke="#fff" stroke-width="1.1">
              <ellipse cx="8" cy="8" rx="3" ry="6.4"/>
              <path d="M1.5 8h13M2.6 4.6h10.8M2.6 11.4h10.8"/>
            </g>
          </svg>
          www.marissatollandlcsw.example
        </span>
        <span class="contact-bar__item">
          <svg class="contact-bar__icon" viewBox="0 0 16 16" aria-hidden="true">
            <rect x="1" y="3" width="14" height="10" rx="1.5"/>
            <path d="M2 4.2l6 4.6 6-4.6" fill="none" stroke="#fff" stroke-width="1.2"/>
          </svg>
          therapy@marissatollandlcsw.example
        </span>
      </address>
      <div class="footer-band" aria-hidden="true">
        <div class="footer-band__rule"></div>
        <div class="footer-band__gap"></div>
        <div class="footer-band__fill"></div>
      </div>
    </footer>
  </main>
</body>
</html>
```